Business cards and stationary for mobile catering company
Harvest Kettle
Bright & Fun-filled
Martin Probert
Mobile Catering Proprietor
Fernleigh
Corwen Terrace
Ashmere
Wealdshire
KT9 4LP
martin@harvestkettle.co.uk
www.harvestkettle.co.uk
we would like a simple but stylish desing in keeping with our logo
THIS IS OUR LOGO
the . eps file if required

```html
<!DOCTYPE html>
<html lang="en">
<head>
<meta charset="utf-8">
<title>Harvest Kettle – Business Cards</title>
<link rel="stylesheet" href="https://fonts.googleapis.com/css2?family=Cabin:wght@400;600;700&display=swap">
<style>
  :root {
    --backdrop: #8f8f91;
    --lime: #8cc34a;
    --cocoa: #5b3a22;
    --paper: #ffffff;
    --ink-light: #ffffff;
  }
  html, body {
    margin: 0;
    width: 1200px;
    height: 895px;
    overflow: hidden;
    background: var(--backdrop);
    font-family: "Cabin", sans-serif;
  }
  .sheet {
    position: relative;
    width: 1200px;
    height: 895px;
  }
  .card {
    position: absolute;
    width: 540px;
    height: 309px;
    overflow: hidden;
    border-radius: 3px;
    box-shadow: 0 6px 18px rgba(0,0,0,0.25);
  }
  .card--front { left: 40px; top: 293px; }
  .card--back { left: 620px; top: 293px; background: var(--lime); }
  .card__art {
    position: absolute;
    inset: 0;
    width: 100%;
    height: 100%;
  }

  /* Front */
  .brand {
    position: absolute;
    top: 44px;
    left: 0;
    right: 0;
    display: flex;
    justify-content: center;
    align-items: center;
    gap: 10px;
  }
  .brand__dot {
    width: 22px;
    height: 22px;
    border-radius: 50%;
    background: var(--cocoa);
  }
  .brand__name {
    font-size: 34px;
    font-weight: 600;
    color: var(--lime);
    letter-spacing: 0.2px;
  }
  .holder {
    position: absolute;
    top: 142px;
    left: 0;
    right: 0;
    text-align: center;
    color: var(--ink-light);
  }
  .holder__name {
    font-size: 15px;
    font-weight: 700;
    margin: 0;
  }
  .holder__role {
    font-size: 11px;
    margin: 2px 0 0;
  }
  .address {
    position: absolute;
    top: 190px;
    right: 290px;
    margin: 0;
    font-style: normal;
    font-size: 10.5px;
    line-height: 1.45;
    color: var(--ink-light);
    text-align: right;
  }
  .contacts {
    position: absolute;
    top: 190px;
    left: 290px;
    margin: 0;
    padding: 0;
    list-style: none;
    font-size: 10.5px;
    line-height: 1.45;
    color: var(--ink-light);
  }
  .contacts li {
    display: flex;
    align-items: center;
    gap: 6px;
  }
  .contacts svg { width: 11px; height: 11px; flex: none; }

  /* Back */
  .mark {
    position: absolute;
    top: 26px;
    left: 0;
    right: 0;
    display: flex;
    flex-direction: column;
    align-items: center;
    gap: 14px;
  }
  .mark__circle {
    width: 150px;
    height: 150px;
    border-radius: 50%;
    background: var(--cocoa);
  }
  .mark__name {
    font-size: 30px;
    font-weight: 600;
    color: var(--cocoa);
  }
  .back-web {
    position: absolute;
    right: 28px;
    bottom: 22px;
    margin: 0;
    font-size: 13px;
    color: var(--ink-light);
    letter-spacing: 0.6px;
  }
</style>
</head>
<body>
<main class="sheet">

  <section class="card card--front" aria-label="Business card front">
    <svg class="card__art" viewBox="0 0 540 309" preserveAspectRatio="none" aria-hidden="true">
      <rect width="540" height="309" fill="var(--paper)"/>
      <path d="M0,116 C180,150 360,112 540,64 L540,309 L0,309 Z" fill="var(--lime)"/>
      <path d="M0,104 C180,138 360,100 540,52 L540,64 C360,112 180,150 0,116 Z" fill="var(--cocoa)"/>
      <path d="M0,268 C180,300 360,250 540,272 L540,280 C360,258 180,308 0,276 Z" fill="var(--paper)"/>
      <path d="M0,276 C180,308 360,258 540,280 L540,286 C360,264 180,314 0,282 Z" fill="var(--cocoa)"/>
    </svg>

    <div class="brand">
      <span class="brand__dot"></span>
      <span class="brand__name">Harvest Kettle</span>
    </div>

    <div class="holder">
      <p class="holder__name">Martin Probert</p>
      <p class="holder__role">Mobile Catering Proprietor</p>
    </div>

    <address class="address">
      Fernleigh, Corwen Terrace<br>
      Ashmere, Wealdshire<br>
      KT9 4LP
    </address>

    <ul class="contacts">
      <li>
        <svg viewBox="0 0 12 12"><path d="M3 1 L5 3.5 L4 5 C4.6 6.4 5.6 7.4 7 8 L8.5 7 L11 9 L10 11 C5.5 11 1 6.5 1 2 Z" fill="#fff"/></svg>
        07700 900316
      </li>
      <li>
        <svg viewBox="0 0 12 12"><rect x="1" y="2.5" width="10" height="7" fill="none" stroke="#fff" stroke-width="1.2"/><path d="M1 2.5 L6 7 L11 2.5" fill="none" stroke="#fff" stroke-width="1.2"/></svg>
        martin@harvestkettle.co.uk
      </li>
      <li>
        <svg viewBox="0 0 12 12"><circle cx="6" cy="6" r="5" fill="none" stroke="#fff" stroke-width="1.1"/><ellipse cx="6" cy="6" rx="2.2" ry="5" fill="none" stroke="#fff" stroke-width="1"/><path d="M1 6 H11" stroke="#fff" stroke-width="1"/></svg>
        www.harvestkettle.co.uk
      </li>
    </ul>
  </section>

  <section class="card card--back" aria-label="Business card back">
    <div class="mark">
      <span class="mark__circle"></span>
      <span class="mark__name">Harvest Kettle</span>
    </div>
    <p class="back-web">www.harvestkettle.co.uk</p>
  </section>

</main>
</body>
</html>
```